Cocktail Syrup / Mixers. Modern clean professional

Looking to design a line of cocktail syrups. The goal would have it look high end. Flavors include Pina Colada, Blue Hawaiian, Margaretta, and other fruit flavors. Labels should be hip, and modern looking. I attached the coffee blends as an example but would like it to be very different from these.

Target Market(s)

18-30

Industry/Entity Type

Food Production

Font styles to use
Serif
Sans Serif

Colors

Designer to choose colors to be used in the design.

Requirements
Must have
• Logo must be centered with the name of the flavor. The label size is 5" height, 8" wide.
Nice to have
• Fruit or some sort of design including different colors per label.
Should not have
• open to everything

```html
<!DOCTYPE html>
<html lang="en">
<head>
<meta charset="utf-8">
<title>Tiki Pour Flavored Syrups – Label Line</title>
<link href="https://fonts.googleapis.com/css2?family=Josefin+Sans:wght@400;600;700&display=swap" rel="stylesheet">
<style>
  :root {
    --canvas: #ffffff;
    --label-white: #ffffff;
    --ink: #1e1e1e;
    --ink-soft: #3a3a3a;
    --colada-main: #e6d21c;
    --colada-light: #f3ea7a;
    --colada-deep: #c9b80e;
    --hawaiian-main: #2fb1bd;
    --hawaiian-light: #8fd8dd;
    --hawaiian-deep: #1a8d98;
    --margarita-main: #7cc242;
    --margarita-light: #b8e08a;
    --margarita-deep: #4f9a2a;
    --fruit-pineapple: #f2c531;
    --fruit-leaf: #4d8f2e;
    --fruit-lime: #8acb3f;
    --umbrella: #8a7bd6;
  }
  * { margin: 0; padding: 0; box-sizing: border-box; }
  html, body {
    width: 1200px;
    height: 1200px;
    overflow: hidden;
    background: var(--canvas);
  }
  .label-line {
    width: 1200px;
    height: 1200px;
    display: flex;
    justify-content: center;
    align-items: center;
    gap: 40px;
  }
  .label {
    --main: var(--colada-main);
    --light: var(--colada-light);
    --deep: var(--colada-deep);
    position: relative;
    width: 340px;
    height: 620px;
    background: var(--label-white);
    box-shadow: 0 2px 14px rgba(0,0,0,0.12);
    overflow: hidden;
    font-family: "Josefin Sans", sans-serif;
    color: var(--ink);
  }
  .label--hawaiian { --main: var(--hawaiian-main); --light: var(--hawaiian-light); --deep: var(--hawaiian-deep); }
  .label--margarita { --main: var(--margarita-main); --light: var(--margarita-light); --deep: var(--margarita-deep); }

  .label__crown-pattern {
    position: absolute;
    top: 0; left: 0;
    width: 100%;
    height: 140px;
    background: linear-gradient(180deg, var(--main) 0%, var(--light) 55%, rgba(255,255,255,0) 100%);
  }
  .label__brand {
    position: absolute;
    top: 200px;
    width: 100%;
    display: flex;
    justify-content: center;
    align-items: center;
    gap: 10px;
  }
  .label__brand-dot {
    width: 16px; height: 16px;
    border-radius: 50%;
    background: var(--ink);
  }
  .label__brand-name {
    font-size: 44px;
    font-weight: 700;
    letter-spacing: 0.5px;
    color: var(--ink);
  }
  .label__fruit-art {
    position: absolute;
    top: 310px;
    left: 20px;
    width: 300px;
    height: 180px;
    border-radius: 6px;
  }
  .label--colada .label__fruit-art,
  .label--hawaiian .label__fruit-art {
    background: linear-gradient(120deg, var(--fruit-leaf) 0%, var(--fruit-pineapple) 45%, #efe6d4 70%, var(--umbrella) 100%);
  }
  .label--margarita .label__fruit-art {
    background: linear-gradient(120deg, var(--fruit-lime) 0%, var(--margarita-light) 55%, var(--umbrella) 100%);
  }
  .label__flavor {
    position: absolute;
    top: 500px;
    width: 100%;
    text-align: center;
    font-size: 34px;
    font-weight: 600;
    letter-spacing: 1px;
    line-height: 46px;
    color: var(--ink);
  }
  .label__info-band {
    position: absolute;
    top: 548px;
    left: 0;
    width: 100%;
    height: 58px;
    background: linear-gradient(90deg, var(--deep) 0%, var(--main) 30%, var(--light) 50%, var(--main) 70%, var(--deep) 100%);
    display: flex;
    flex-direction: column;
    justify-content: center;
    align-items: center;
    gap: 3px;
  }
  .label__type {
    font-size: 14px;
    font-weight: 400;
    color: var(--ink-soft);
    letter-spacing: 0.3px;
  }
  .label__volume {
    font-size: 13px;
    font-weight: 400;
    color: var(--ink-soft);
  }
</style>
</head>
<body>
  <main class="label-line">
    <article class="label label--colada">
      <div class="label__crown-pattern" role="img" aria-label="Yellow geometric triangle pattern"></div>
      <div class="label__brand"><span class="label__brand-dot"></span><span class="label__brand-name">Tiki Pour</span></div>
      <div class="label__fruit-art" role="img" aria-label="Illustration of pineapple, split coconut, palm leaf and purple cocktail umbrella"></div>
      <h2 class="label__flavor">PINA COLADA</h2>
      <div class="label__info-band">
        <span class="label__type">FLAVORED SYRUP</span>
        <span class="label__volume">25.36 fl oz (750ml)</span>
      </div>
    </article>

    <article class="label label--hawaiian">
      <div class="label__crown-pattern" role="img" aria-label="Teal geometric triangle pattern"></div>
      <div class="label__brand"><span class="label__brand-dot"></span><span class="label__brand-name">Tiki Pour</span></div>
      <div class="label__fruit-art" role="img" aria-label="Illustration of pineapple, split coconut, palm leaf and purple cocktail umbrella"></div>
      <h2 class="label__flavor">BLUE HAWAIIAN</h2>
      <div class="label__info-band">
        <span class="label__type">FLAVORED SYRUP</span>
        <span class="label__volume">25.36 fl oz (750ml)</span>
      </div>
    </article>

    <article class="label label--margarita">
      <div class="label__crown-pattern" role="img" aria-label="Green geometric triangle pattern"></div>
      <div class="label__brand"><span class="label__brand-dot"></span><span class="label__brand-name">Tiki Pour</span></div>
      <div class="label__fruit-art" role="img" aria-label="Illustration of whole and sliced limes, palm leaf and purple cocktail umbrella"></div>
      <h2 class="label__flavor">MARGARETTA</h2>
      <div class="label__info-band">
        <span class="label__type">FLAVORED SYRUP</span>
        <span class="label__volume">25.36 fl oz (750ml)</span>
      </div>
    </article>
  </main>
</body>
</html>
```